Brightway Supply Postcard Mailout

Brightway Supply is a dental supplier. We supply promotional products and marketing to dental clinics to attract new patients and retain existing.

Purpose:
We are needing a post card designed to mail out to practices with the hope to gain their business.
We are giving away 200 free dental supply bags to any first order.
- Utilise free bags
- Obtain new Accounts

Size:
POSTCARD

Images:
Dental Bags - see attached
Brightway Supply Logo - see attached variations

Front of Card:
Eye-catching and attention grabbing, force to continue reading.

Back of card:
- Hero being the 200 x FREE Dental Supply Bags
-Leave room for address label and stamp on right side

Post card design needs to compliment our colour/branding of our logo.

Target Market(s)

Dental Practices - Owners, Doctors, & Receptionists

Font styles to use
Sans Serif

Colors

Designer to choose colors to be used in the design.

Requirements
Must have
• Call of Action
Nice to have
• Corporate look with a modern friendly feel.
• Playful wording
Should not have
• No cartoon imagery.

```html
<!DOCTYPE html>
<html lang="en">
<head>
<meta charset="utf-8">
<title>Brightway Supply Postcard Mailout</title>
<link rel="stylesheet" href="https://fonts.googleapis.com/css2?family=Anton&family=Michroma&family=Roboto:wght@500&display=swap">
<style>
  :root {
    --board: #3a3a3c;
    --green-dark: #137a35;
    --green: #1f9a45;
    --green-light: #3dbb55;
    --ink: #111111;
    --white: #ffffff;
    --heading-green: #1c6e34;
  }
  * { margin: 0; padding: 0; box-sizing: border-box; }
  html, body { width: 903px; height: 1200px; overflow: hidden; background: var(--board); }
  .board { position: relative; width: 903px; height: 1200px; }
  .card { position: absolute; left: 96px; width: 712px; height: 509px; overflow: hidden; background: var(--white); }
  .card--front { top: 74px; background: linear-gradient(180deg, #8ed98f 0%, #c7e9b0 40%, #f3faf0 62%, #ffffff 75%); }
  .card--back { top: 618px; background: linear-gradient(160deg, #f4fbf0 0%, #eaf5e2 30%, #f6fafb 60%, #ffffff 100%); }
  .facets { position: absolute; left: 0; top: 0; width: 712px; height: 200px; }

  .kicker { position: absolute; top: 44px; left: 0; width: 100%; text-align: center; font-family: "Michroma", sans-serif; font-size: 16px; letter-spacing: -0.5px; color: var(--green-dark); -webkit-text-stroke: 0.8px var(--green-dark); }
  .headline { position: absolute; top: 68px; left: 0; width: 100%; text-align: center; font-family: "Anton", sans-serif; font-weight: 400; font-size: 86px; line-height: 96px; letter-spacing: 0.5px; color: var(--green); background: linear-gradient(180deg, #3cbf55 0%, #128030 100%); -webkit-background-clip: text; background-clip: text; -webkit-text-fill-color: transparent; filter: drop-shadow(0 0 1px #fff) drop-shadow(0 0 1px #fff) drop-shadow(1px 2px 2px rgba(0,0,0,.2)); }
  .offer-pill { position: absolute; left: 40px; top: 169px; width: 630px; height: 38px; border-radius: 19px; background: linear-gradient(180deg, #3dbb55 0%, #14843a 100%); display: flex; align-items: center; justify-content: center; font-family: "Michroma", sans-serif; font-size: 17px; color: var(--white); letter-spacing: -0.5px; -webkit-text-stroke: 0.8px var(--white); }

  .product-shot { position: absolute; left: 80px; top: 229px; width: 368px; height: 166px; background: linear-gradient(135deg, #eef1f6 0%, #dfe4ec 50%, #f4f5f8 100%); box-shadow: 2px 3px 6px rgba(0,0,0,.35); }

  .benefit { position: absolute; left: 487px; width: 225px; }
  .benefit svg { position: absolute; inset: 0; width: 100%; height: 100%; }
  .benefit__text { position: absolute; left: 12px; right: 0; top: 0; bottom: 0; display: flex; align-items: center; justify-content: center; text-align: center; font-family: "Anton", sans-serif; font-size: 33px; line-height: 38px; color: var(--white); }
  .benefit--bags { top: 226px; height: 142px; }
  .benefit--accounts { top: 368px; height: 141px; }

  .brand { position: absolute; left: 82px; top: 410px; width: 380px; }
  .brand__name { display: block; white-space: nowrap; font-family: "Anton", sans-serif; font-size: 44px; line-height: 54px; color: var(--ink); }
  .brand__tagline { display: block; margin-top: 2px; padding-left: 4px; white-space: nowrap; font-family: "Roboto", sans-serif; font-weight: 500; font-size: 13px; color: var(--ink); }

  .portrait { position: absolute; left: 0; top: 0; width: 440px; height: 509px; background: radial-gradient(ellipse 60% 55% at 32% 42%, #efcfbd 0%, #e9c3ae 40%, rgba(240,214,200,.55) 70%, rgba(246,250,244,0) 100%); }
  .stamp-box { position: absolute; left: 597px; top: 40px; width: 87px; height: 88px; border: 1.5px solid #333; }
  .back-heading { position: absolute; left: 270px; top: 126px; font-family: "Anton", sans-serif; font-weight: 400; font-size: 32px; line-height: 40px; color: var(--heading-green); }
  .address-line { position: absolute; left: 444px; width: 240px; height: 0; border-top: 1.5px solid #333; }
</style>
</head>
<body>
<div class="board">
  <section class="card card--front">
    <svg class="facets" viewBox="0 0 712 200" aria-hidden="true">
      <polygon points="0,0 160,0 60,90" fill="#2f9e5a" opacity=".25"/>
      <polygon points="120,0 330,0 230,60" fill="#1f7a4a" opacity=".18"/>
      <polygon points="420,0 600,0 520,70" fill="#2a8f55" opacity=".22"/>
      <polygon points="560,0 712,0 712,110" fill="#1e6e45" opacity=".25"/>
      <polygon points="0,60 90,130 0,170" fill="#ffffff" opacity=".15"/>
      <polygon points="600,40 712,120 640,160" fill="#ffffff" opacity=".15"/>
    </svg>
    <p class="kicker">WE ARE GIVING AWAY</p>
    <h1 class="headline">200 FREE DENTAL</h1>
    <div class="offer-pill">SUPPLY BAGS TO ANY FIRST ORDER.</div>

    <div class="product-shot" role="img" aria-label="Photo of a clear dental supply bag printed with a toothbrush pattern"></div>

    <div class="benefit benefit--bags">
      <svg viewBox="0 0 225 142" preserveAspectRatio="none" aria-hidden="true">
        <defs><linearGradient id="gGreen" x1="0" y1="0" x2="0" y2="1"><stop offset="0" stop-color="#2fb04e"/><stop offset="1" stop-color="#127a37"/></linearGradient></defs>
        <polygon points="12,0 225,0 225,142 12,142 0,71" fill="url(#gGreen)"/>
      </svg>
      <p class="benefit__text">UTILISE<br>FREE BAGS</p>
    </div>
    <div class="benefit benefit--accounts">
      <svg viewBox="0 0 225 141" preserveAspectRatio="none" aria-hidden="true">
        <defs><linearGradient id="gBlue" x1="0" y1="0" x2="0" y2="1"><stop offset="0" stop-color="#1aa7a2"/><stop offset="1" stop-color="#1a6fca"/></linearGradient></defs>
        <polygon points="12,0 225,0 225,141 12,141 0,70" fill="url(#gBlue)"/>
      </svg>
      <p class="benefit__text">OBTAIN NEW<br>ACCOUNTS</p>
    </div>

    <div class="brand">
      <span class="brand__name">Brightway Supply</span>
      <span class="brand__tagline">Better Supplies. Brighter Smiles.</span>
    </div>
  </section>

  <section class="card card--back">
    <div class="portrait" role="img" aria-label="Close-up photo of a smiling woman resting her chin on her hand"></div>
    <div class="stamp-box" aria-label="Stamp area"></div>
    <h2 class="back-heading">HERO BEING THE<br>200 X FREE DENTAL<br>SUPPLY BAGS</h2>
    <span class="address-line" style="top:348px"></span>
    <span class="address-line" style="top:392px"></span>
    <span class="address-line" style="top:437px"></span>
  </section>
</div>
</body>
</html>
```